Marigold Treehouse WordPress Website

Wordpress/Divi website for our daycare/learning center. Please see directions and layout documents.
Target Market(s)
Primary Market is for existing clientele. Parents of young children age 1-7 yrs old. Parents are well educated, between 23-40 years of age.
Industry/Entity Type
Early Learning Center
Coding
Coded - Design and coding required
Font styles to use
Sans Serif
Requirements
Must have
- • The website MUST be responsive and optimized for mobile devices like iPads and cellphones.
• Use logo from file.
• Pictures of people, they should be of children/staff in our target markets.
• Utuilize linking to Plumcrate for Scheduling and News
• Social media links in all pages.
• Include Chamber of Commerce logo in all pages.
• Use placeholder pics wherever you feel a pic should be
Nice to have
- LOOK AND FEEL
Please do NOT copy, but https://www.ostrowacademy.example is an example of overall look and feel. User (Parent) friendly, Clean, easy to navigate, visually appealing without being cluttered. Colors should be pleasing to the eye (No grays)
Should not have
- NO custom coding. Site must be 100% constructed using WordPress/Copperleaf Layouts/Divi. Site will be stored at NimbuVault Supported Wordpress.

```html
<!DOCTYPE html>
<html lang="en">
<head>
<meta charset="utf-8">
<title>Marigold Treehouse – Early Childhood Learning Centers</title>
<link rel="stylesheet" href="https://fonts.googleapis.com/css2?family=Montserrat:wght@300;400;500;600&family=Poppins:wght@500;600&display=swap">
<style>
:root{
  --blue:#2d6fcf;
  --gold:#fbbc3c;
  --ink:#2b2b2b;
  --text:#4a4a4a;
  --band:#eef3fb;
  --grey-band:#f2f2f2;
  --white:#ffffff;
}
*{box-sizing:border-box;margin:0;padding:0}
html,body{width:1200px;height:3426px;overflow:hidden;background:var(--white)}
body{font-family:"Montserrat",sans-serif;color:var(--text);font-weight:300}
section,header,footer{position:relative;overflow:hidden}
.wrap{width:1000px;margin:0 auto;position:relative}
h2.section-title{font-family:"Poppins",sans-serif;font-weight:600;font-size:24px;line-height:32px;color:var(--ink);text-align:center;position:relative;padding-bottom:14px}
h2.section-title::after{content:"";position:absolute;left:50%;bottom:0;width:32px;height:4px;border-radius:2px;background:var(--blue);transform:translateX(-50%)}
.btn{display:inline-block;background:var(--gold);color:var(--white);font-weight:500;font-size:15px;border-radius:6px;padding:10px 26px;text-decoration:none}
.btn-blue{display:inline-block;background:var(--blue);color:var(--white);font-weight:600;border-radius:6px;padding:9px 16px;font-size:15px;text-decoration:none;white-space:nowrap}
.photo{display:block}

/* Navigation */
.site-nav{height:66px;background:var(--blue)}
.site-nav .wrap{display:flex;align-items:center;justify-content:space-between;height:66px}
.brand{background:var(--white);border-radius:6px;height:58px;width:94px;display:flex;align-items:center;justify-content:center;font-weight:600;font-size:11px;color:var(--blue);text-align:center;line-height:1.25;padding:0 6px}
.nav-links{display:flex;gap:30px;list-style:none}
.nav-links a{color:var(--white);text-decoration:none;font-size:13px;font-weight:500}

/* Hero */
.hero{height:434px;background:linear-gradient(90deg,#f4f4f4 0%,#f1f1f1 38%,#e9e4dc 62%,#efe9e1 100%)}
.hero-photo{position:absolute;right:30px;top:0;width:600px;height:434px;background:radial-gradient(ellipse at 45% 45%,#f0dccb 0%,#e9ddd0 35%,rgba(240,238,235,0) 70%)}
.hero-copy{position:absolute;left:157px;top:92px;width:460px}
.hero-copy h1{font-family:"Poppins",sans-serif;font-weight:500;font-size:26px;line-height:34px;color:var(--ink);margin-bottom:24px;white-space:nowrap}
.hero-copy p{font-size:16px;line-height:25px;margin-bottom:36px;width:430px}
.hero-arrow{position:absolute;top:260px}
.hero-arrow.left{left:100px}
.hero-arrow.right{right:100px}

/* Locations */
.locations{height:560px;padding-top:54px}
.loc-grid{display:flex;justify-content:space-between;margin-top:26px}
.loc{width:467px}
.loc h3{font-family:"Poppins",sans-serif;font-weight:500;font-size:16px;color:var(--ink);text-align:center;margin-bottom:14px}
.loc .photo{height:250px}
.loc-newburgh{background:linear-gradient(180deg,#5a8fd8 0%,#a9c6ec 40%,#8f8877 62%,#2d2b28 100%)}
.loc-windsor{background:linear-gradient(180deg,#dde2e8 0%,#c7cbc6 30%,#c8b38f 55%,#4c4c4f 75%,#5a5c60 100%)}
.loc-info{margin-top:22px;font-size:14.5px;line-height:22.5px}
.loc-info b{font-weight:600;color:var(--ink)}
.directions{display:inline-flex;align-items:center;gap:8px;margin-top:10px;color:var(--blue);font-weight:500;font-size:15px;text-decoration:none}

/* Philosophy */
.philosophy{height:620px;padding-top:40px}
.phil-grid{display:flex;justify-content:space-between;margin-top:28px}
.phil-text{width:470px;font-size:14px;line-height:22px}
.phil-text p+p{margin-top:22px}
.collage{width:500px;height:490px;position:relative}
.collage .photo{position:absolute;border:2px solid var(--white);box-shadow:0 1px 4px rgba(0,0,0,.15)}
.c1{left:50px;top:0;width:410px;height:255px;background:linear-gradient(120deg,#e24a3a 0%,#f3c64a 35%,#f4efe8 60%,#6fa4c9 100%)}
.c2{left:195px;top:190px;width:305px;height:190px;background:linear-gradient(135deg,#c9d2a8 0%,#f0c6a8 40%,#e13b7a 75%,#8a9a6a 100%)}
.c3{left:0;top:290px;width:305px;height:192px;background:linear-gradient(120deg,#7db7d6 0%,#f2d2b0 40%,#e8c24a 70%,#5f9bd8 100%)}

/* Team */
.team{height:574px;padding-top:40px}
.team-grid{display:flex;justify-content:space-between;margin-top:32px}
.member{width:290px;text-align:center}
.member .photo{height:167px}
.m1{background:linear-gradient(180deg,#dadada,#cfcac3)}
.m2{background:linear-gradient(180deg,#7fa6c6,#9bb6cd)}
.m3{background:linear-gradient(180deg,#e9ebee,#dcdfe3)}
.member h3{font-weight:600;font-size:14.5px;color:var(--ink);margin-top:23px;line-height:20px}
.member h3 span{font-weight:400;display:block}
.member p{font-size:14.5px;line-height:22.5px;margin:12px 0 22px}

/* App band */
.app-band{height:201px;background:var(--band)}
.app-band .wrap{padding-top:24px}
.app-brand{display:flex;align-items:center;gap:10px;font-weight:500;font-size:38px;color:var(--blue);line-height:44px}
.app-brand i{display:block;width:30px;height:30px;border-radius:50%;background:var(--gold)}
.app-row{display:flex;justify-content:space-between;align-items:flex-start;margin-top:22px}
.app-row p{width:800px;font-size:15px;line-height:22.5px}
.app-row .btn-blue{margin-top:4px}

/* Services */
.services{height:512px;padding-top:66px}
.svc-grid{display:flex;justify-content:space-between}
.svc{width:467px;text-align:center}
.svc .photo{height:250px;margin:34px 0 34px}
.s1{background:linear-gradient(120deg,#e8e1d6 0%,#c9a896 40%,#f1c2a9 60%,#e9bf7a 100%)}
.s2{background:linear-gradient(120deg,#e6e0da 0%,#b88a70 40%,#f0bfc4 65%,#d9c3ad 100%)}

/* Partners */
.partners{height:109px;background:var(--grey-band);display:flex;justify-content:space-around;align-items:center;padding:0 180px}
.badge{width:160px;height:60px;border-radius:6px}
.badge-chamber{background:#d6d0bf}
.badge-accredit{background:#cfdaf0}

/* Footer */
.site-footer{height:350px;background:var(--blue);color:var(--white)}
.footer-grid{display:flex;justify-content:space-between;padding-top:30px;height:304px}
.footer-col h4{font-family:"Poppins",sans-serif;font-weight:600;font-size:15px;margin-bottom:6px}
.footer-col p{font-size:14.5px;line-height:22.5px}
.socials{display:flex;gap:8px;margin:10px 0 20px}
.socials span{width:24px;height:24px;border:2px solid var(--white);border-radius:4px}
.footer-mid{width:430px;text-align:center;padding-top:20px}
.footer-brand{font-weight:600;font-size:24px;line-height:30px;margin-bottom:70px}
.footer-mid p{font-size:14.5px;line-height:22.5px;text-align:left;margin-left:-30px}
.quick ul{list-style:none}
.quick li{font-size:14.5px;line-height:33.5px}
.copyright{border-top:1px solid rgba(255,255,255,.35);text-align:center;font-size:14.5px;line-height:46px}
</style>
</head>
<body>

<header class="site-nav">
  <div class="wrap">
    <div class="brand">Marigold Treehouse</div>
    <ul class="nav-links">
      <li><a href="#">Our Team</a></li>
      <li><a href="#">Our Philosophy</a></li>
      <li><a href="#">Flex Scheduling</a></li>
      <li><a href="#">Sitter Service</a></li>
      <li><a href="#">Awards/Accolades</a></li>
      <li><a href="#">Join Our Team</a></li>
    </ul>
  </div>
</header>

<section class="hero">
  <div class="hero-photo" role="img" aria-label="Toddler stacking wooden blocks at a high chair"></div>
  <svg class="hero-arrow left" width="26" height="46" viewBox="0 0 26 46"><path d="M22 3 4 23l18 20" fill="none" stroke="#b9b9b9" stroke-width="4"/></svg>
  <svg class="hero-arrow right" width="26" height="46" viewBox="0 0 26 46"><path d="M4 3l18 20L4 43" fill="none" stroke="#b9b9b9" stroke-width="4"/></svg>
  <div class="hero-copy">
    <h1>Early Childhood Learning Centers</h1>
    <p>It is our goal at Marigold Treehouse to make each child feel safe and secure, while exposing them to appropriate developmental skills and building a positive self-concept.</p>
    <a class="btn" href="#">Learn More</a>
  </div>
</section>

<section class="locations">
  <div class="wrap">
    <h2 class="section-title">Locations</h2>
    <div class="loc-grid">
      <div class="loc">
        <h3>Elmbrook</h3>
        <div class="photo loc-newburgh" role="img" aria-label="Elmbrook two-storey school building under a blue sky"></div>
        <div class="loc-info">
          <b>Hours:</b> 6:30 AM - 6:00 PM<br>
          Serving children 8 weeks to 12 years<br>
          <b>Address:</b> 4170 Orchard Road, Elmbrook, NY 10990
        </div>
        <a class="directions" href="#">Directions <svg width="16" height="10" viewBox="0 0 16 10"><path d="M0 5h14M10 1l4 4-4 4" fill="none" stroke="#2d6fcf" stroke-width="1.6"/></svg></a>
      </div>
      <div class="loc">
        <h3>Westhaven</h3>
        <div class="photo loc-windsor" role="img" aria-label="Westhaven single-storey school building with parking lot"></div>
        <div class="loc-info">
          <b>Hours:</b> 6:30 AM - 6:00 PM<br>
          Serving children 8 weeks to 12 years<br>
          <b>Address:</b> 318 Meadow Lane, Westhaven, NY 10991
        </div>
        <a class="directions" href="#">Directions <svg width="16" height="10" viewBox="0 0 16 10"><path d="M0 5h14M10 1l4 4-4 4" fill="none" stroke="#2d6fcf" stroke-width="1.6"/></svg></a>
      </div>
    </div>
  </div>
</section>

<section class="philosophy">
  <div class="wrap">
    <h2 class="section-title">Our Philosophy</h2>
    <div class="phil-grid">
      <div class="phil-text">
        <p>It is our goal at Marigold Treehouse to make each child feel safe and secure, while exposing them to appropriate developmental skills and building a positive self-concept. We encourage children to take risks and learn from their mistakes in both academic and social settings. We use a positive behavior approach which consists of specific praise, modeling appropriate behaviors, and providing children with acceptable choices. We teach children to develop behavior habits and attitudes that will allow them to interact well with others in school and throughout life.</p>
        <p>At Marigold Treehouse, we strive to prepare our children for the next step they will be taking-whether it be moving from the infant room to the toddler room, or leaving our pre-kindergarten program to enter kindergarten in another school. Children experience growth and learning in their social- emotional, physical, language, and cognitive development. We provide children with the tools they need to be successful and encourage them to use these tools in a way that works best for them. Thoughout every child’s experience at Marigold Treehouse, families will feel supported and nurtured in their child rearing efforts.</p>
      </div>
      <div class="collage">
        <div class="photo c1" role="img" aria-label="Smiling girl lying on the floor of a colorful classroom"></div>
        <div class="photo c2" role="img" aria-label="Laughing toddler in a pink jacket on a playground swing"></div>
        <div class="photo c3" role="img" aria-label="Young boy playing with colorful building blocks"></div>
      </div>
    </div>
  </div>
</section>

<section class="team">
  <div class="wrap">
    <h2 class="section-title">Our Team</h2>
    <div class="team-grid">
      <div class="member">
        <div class="photo m1" role="img" aria-label="Portrait of owner Dana Whitcombe"></div>
        <h3>Dana Whitcombe,<span>Owner</span></h3>
        <p>Dana purchased Marigold Treehouse in April 2005. Since then she has expanded the school with a large addition, doubling the number of students and families served.</p>
        <a class="btn" href="#">Learn More</a>
      </div>
      <div class="member">
        <div class="photo m2" role="img" aria-label="Portrait of director Marisa Delvane"></div>
        <h3>Marisa Delvane,<span>Director @ Marigold Treehouse</span></h3>
        <p>Marisa began working as the Director at Marigold Treehouse in April 2005. Prior to her role as Director, she taught in the Linden Falls School District for two years.</p>
        <a class="btn" href="#">Learn More</a>
      </div>
      <div class="member">
        <div class="photo m3" role="img" aria-label="Portrait of director Noelle Ravensbrook"></div>
        <h3>Noelle Ravensbrook,<span>Director @ Marigold Treehouse on 32</span></h3>
        <p>Noelle has been working with Marigold Treehouse since 2010. She became director of Marigold Treehouse on 32 in 2018. She holds two associates degrees, in Childcare and in Business.</p>
        <a class="btn" href="#">Learn More</a>
      </div>
    </div>
  </div>
</section>

<section class="app-band">
  <div class="wrap">
    <div class="app-brand"><i></i>Plumcrate</div>
    <div class="app-row">
      <p>We recently started using Plumcrate, a tool for classroom management, communication, photos, videos, online bill pay, and much more. Plumcrate is the industry leader in early education, proven to save time for staff, allowing for measurably more time with students, while also delivering a much better experience for parents.</p>
      <a class="btn-blue" href="#">Download App</a>
    </div>
  </div>
</section>

<section class="services">
  <div class="wrap svc-grid">
    <div class="svc">
      <h2 class="section-title">Flex Scheduling</h2>
      <div class="photo s1" role="img" aria-label="Children drawing with crayons at a classroom table with a teacher"></div>
      <a class="btn" href="#">Learn More</a>
    </div>
    <div class="svc">
      <h2 class="section-title">Sitter Services</h2>
      <div class="photo s2" role="img" aria-label="Sitter playing with a young girl and toy blocks at a table"></div>
      <a class="btn" href="#">Learn More</a>
    </div>
  </div>
</section>

<section class="partners">
  <div class="badge badge-chamber" role="img" aria-label="Chamber of Commerce membership badge"></div>
  <div class="badge badge-accredit" role="img" aria-label="Early childhood accreditation badge"></div>
</section>

<footer class="site-footer">
  <div class="wrap footer-grid">
    <div class="footer-col">
      <h4>Elmbrook</h4>
      <p>P: 555-014-2231<br>F: 555-014-2232</p>
      <div class="socials" aria-label="Social links"><span></span><span></span><span></span></div>
      <h4>Westhaven</h4>
      <p>P: 555-017-8843<br>F: 555-017-8844</p>
      <div class="socials" aria-label="Social links"><span></span><span></span><span></span></div>
    </div>
    <div class="footer-mid">
      <div class="footer-brand">Marigold Treehouse</div>
      <p>It is our goal at Marigold Treehouse to make each child feel safe and secure, while exposing them to appropriate developmental skills and building a positive self-concept. We encourage children to take risks and learn from their mistakes in both academic and social settings.</p>
    </div>
    <div class="footer-col quick">
      <h4>Quick Links</h4>
      <ul>
        <li>Home</li><li>Our Team</li><li>Our Philosophy</li><li>Flex Scheduling</li><li>Sitter Service</li><li>Awards/Accolades</li><li>Join Our Team</li>
      </ul>
    </div>
  </div>
  <div class="copyright">Copyright © 2020 Marigold Treehouse. All rights reserved.</div>
</footer>

</body>
</html>
```